Business Card needed for Drainor, a growing Septic Service company

Drainor, a growing local septic service company in Pennsylvania, needs updated business cards. We'd like the business card to feature our logo and communicate that we provide Septic Pumping, Installations/Repairs, Restroom Rentals, and 24/7 Emergency Service. The business card should be eye-catching, bold, and clean/simple. We have been in business almost 10 years and would like to expand and update our business brand and image.

Target Market(s)

Residential and Commercial, New and Current Homeowners

Industry/Entity Type

Service

Contact Information for Business Card

Contact on the business card should be: Dean Harlow Owner & Operator
Phone: 610-555-0187
Email: service@drainor-example.com
Website: www.drainor-example.com
Address: 812 Millbrook Lane Fernvale PA 17099

Font styles to use
Sans Serif

Colors

Designer to choose colors to be used in the design.

Requirements
Must have
• Feature logo on both side of business card.
Nice to have
• We envision the contact information on one side and our services listed on the other side. Utilize the green from the symbol in our logo as part of the design, overall design color scheme should be white, grey, black.

```html
<!DOCTYPE html>
<html lang="en">
<head>
<meta charset="utf-8">
<title>Drainor Business Card – Front and Back</title>
<link rel="stylesheet" href="https://fonts.googleapis.com/css2?family=Figtree:wght@400;500;600;800&display=swap">
<style>
  :root {
    --stage-top: #5a5a5c;
    --stage-bottom: #39393b;
    --card-white: #ffffff;
    --brand-green: #84c441;
    --pale-green: #eff5e6;
    --ink: #060708;
    --text-grey: #4f4f52;
    --label-white: #ffffff;
  }
  * { box-sizing: border-box; margin: 0; padding: 0; }
  html, body { width: 1200px; height: 1200px; overflow: hidden; }
  body { font-family: "Figtree", "Helvetica Neue", Arial, sans-serif; position: relative; }

  .stage { position: absolute; left: 0; width: 1200px; height: 600px; }
  .stage--front { top: 0; background: var(--stage-top); }
  .stage--back { top: 600px; background: var(--stage-bottom); }

  .side-label {
    position: absolute; left: 24px; top: 20px;
    color: var(--label-white); font-weight: 600; font-size: 17px; letter-spacing: -0.2px;
  }

  .card {
    position: absolute; left: 240px; top: 84px;
    width: 720px; height: 432px;
    background: var(--card-white); overflow: hidden;
  }

  .card__panel { position: absolute; left: 398px; width: 322px; background: var(--pale-green); }
  .card--front .card__panel { top: 129px; height: 285px; border-top-left-radius: 60px; }
  .card--back .card__panel { top: 0; height: 302px; border-bottom-left-radius: 60px; }

  .card__band { position: absolute; left: 0; bottom: 0; width: 720px; height: 18px; display: block; }

  .card__rule { position: absolute; left: 0; top: 265px; width: 392px; height: 1.5px; background: var(--brand-green); }

  .brand { position: absolute; display: flex; align-items: center; gap: 12px; }
  .brand__square { width: 48px; height: 48px; background: var(--brand-green); flex: none; }
  .brand__name { font-weight: 800; font-size: 44px; line-height: 1; color: var(--ink); letter-spacing: 1px; }
  .card--front .brand { left: 392px; top: 48px; }
  .card--back .brand { left: 80px; top: 194px; }

  .person { position: absolute; left: 80px; top: 198px; }
  .person__name { color: var(--brand-green); font-weight: 500; font-size: 24px; line-height: 1.1; }
  .person__role { color: var(--text-grey); font-size: 16.5px; line-height: 1.3; }

  .info-list { position: absolute; left: 56px; top: 283px; list-style: none; }
  .info-list li {
    display: flex; align-items: center; gap: 8px;
    height: 29px; color: var(--text-grey); font-size: 17px;
  }
  .info-list svg { width: 16px; height: 16px; flex: none; fill: var(--brand-green); }

  .service-list { position: absolute; left: 58px; top: 282px; list-style: none; }
  .service-list li {
    display: flex; align-items: center; gap: 12px;
    height: 29px; color: var(--text-grey); font-size: 17px; text-transform: uppercase;
  }
  .service-list .bullet { width: 10px; height: 10px; border-radius: 50%; background: var(--brand-green); flex: none; }
</style>
</head>
<body>

<section class="stage stage--front">
  <h2 class="side-label">FRONT SIDE</h2>
  <article class="card card--front">
    <div class="card__panel"></div>
    <div class="brand">
      <span class="brand__square"></span>
      <span class="brand__name">DRAINOR</span>
    </div>
    <div class="person">
      <p class="person__name">Dean Harlow</p>
      <p class="person__role">Owner &amp; Operator</p>
    </div>
    <div class="card__rule"></div>
    <ul class="info-list">
      <li>
        <svg viewBox="0 0 16 16" aria-hidden="true"><path d="M1 6c0-2 3-3 7-3s7 1 7 3v1h-3.5V5.5h-7V7H1z M3 8h10l1 5H2z"/><circle cx="8" cy="10.5" r="1.6" fill="#fff"/></svg>
        610-555-0187
      </li>
      <li>
        <svg viewBox="0 0 16 16" aria-hidden="true"><path d="M1 3h14v10H1z"/><path d="M1.5 3.5 8 9l6.5-5.5M1.5 12.5 6 8M14.5 12.5 10 8" stroke="#fff" stroke-width="1.1" fill="none"/></svg>
        service@drainor-example.com
      </li>
      <li>
        <svg viewBox="0 0 16 16" aria-hidden="true"><circle cx="8" cy="8" r="7"/><path d="M1 8h14M8 1v14M3 4.5h10M3 11.5h10M8 1c-3 3-3 11 0 14M8 1c3 3 3 11 0 14" stroke="#fff" stroke-width="0.9" fill="none"/></svg>
        www.drainor-example.com
      </li>
      <li>
        <svg viewBox="0 0 16 16" aria-hidden="true"><path d="M8 0.5a5.5 5.5 0 0 1 5.5 5.5c0 4-5.5 9.5-5.5 9.5S2.5 10 2.5 6A5.5 5.5 0 0 1 8 0.5z"/><circle cx="8" cy="6" r="2.2" fill="#fff"/></svg>
        812 Millbrook Lane Fernvale PA 17099
      </li>
    </ul>
    <svg class="card__band" viewBox="0 0 720 18" preserveAspectRatio="none" aria-hidden="true">
      <path d="M0 0H376C384 0 388 4 392 8L404 18H0Z" fill="var(--brand-green)"/>
      <path d="M382 0H720V18H408L396 8C392 4 388 0 382 0Z" fill="var(--ink)"/>
    </svg>
  </article>
</section>

<section class="stage stage--back">
  <h2 class="side-label">BACK SIDE</h2>
  <article class="card card--back">
    <div class="card__panel"></div>
    <div class="brand">
      <span class="brand__square"></span>
      <span class="brand__name">DRAINOR</span>
    </div>
    <div class="card__rule"></div>
    <ul class="service-list">
      <li><span class="bullet"></span>Septic Pumping,</li>
      <li><span class="bullet"></span>Installations/Repairs,</li>
      <li><span class="bullet"></span>Restroom Rentals,</li>
      <li><span class="bullet"></span>24/7 Emergency Service</li>
    </ul>
    <svg class="card__band" viewBox="0 0 720 18" preserveAspectRatio="none" aria-hidden="true">
      <path d="M0 0H376C384 0 388 4 392 8L404 18H0Z" fill="var(--brand-green)"/>
      <path d="M382 0H720V18H408L396 8C392 4 388 0 382 0Z" fill="var(--ink)"/>
    </svg>
  </article>
</section>

</body>
</html>
```